Plume - Stationary Design/Layout

We are a well established clothing design and manufacturing company (Plume Sourcing) based in London UK, with our own factory in Bangladesh, supplying to many fashion retailers and brands. Our factory has very high environmental and ethical standards with people at its heart. Our quality of garments are second to none.
Our new logo has been proudly developed by the Pixel Guild community last month, we are now in the second phase and need the layout designed for our letterheads, double sided business cards, compliment slip and clothing ticket. Feel as creative as you like, but make sure it looks great!!
***The Logo - the logo design and colour is set and should NOT be changed and stay on a dark grey backround. The logo artwork to use is attached.
***Details to use for the business card:
Dorian Hartley
Direct Line: 020 7946 0518
dorian@plumesourcing-mail.test
Plume Sourching Ltd.
58 - 60 Fenwick Row
Hollin . Marbury
NW3 5QJ
Switchboard: 020 7946 0733
Fax: 020 7946 0733
www.plumesourcing-mail.test
***Details to use for the letterhead and compliment slip:
Plume Sourching Ltd.
58 - 60 Fenwick Row
Hollin . Marbury
NW3 5QJ
Fax: 020 7946 0733
www.plumesourcing-mail.test
***Details for Swing Ticket:
Size: 12cm height by 5.5cm width
One side need to have just the logo without the 'Sourcing', on the other it needs to stay blank

```html
<!DOCTYPE html>
<html lang="en">
<head>
<meta charset="utf-8">
<title>Plume Sourcing – Business Card</title>
<link rel="stylesheet" href="https://fonts.googleapis.com/css2?family=Arimo:wght@400;700&family=Didact+Gothic&display=swap">
<style>
  :root {
    --card-bg: #231f20;
    --mint: #b2f0de;
    --grey: #a7a9ac;
    --light-grey: #d9dadb;
    --white: #ffffff;
    --trim: #e7a3a3;
    --page: #ffffff;
    --label: #111111;
  }
  * { margin: 0; padding: 0; box-sizing: border-box; }
  html, body {
    width: 944px; height: 1200px; overflow: hidden;
    background: var(--page);
    font-family: "Arimo", Arial, sans-serif;
  }
  .sheet { position: relative; width: 944px; height: 1200px; }
  .side-label {
    position: absolute; left: 95px;
    font-size: 31px; font-weight: 400; color: var(--label);
    letter-spacing: -0.5px;
  }
  .side-label--front { top: 62px; }
  .side-label--back { top: 615px; }
  .card {
    position: absolute; left: 71px; width: 800px; height: 455px;
    background: var(--card-bg);
    outline: 1px solid var(--trim);
    overflow: hidden;
  }
  .card--front { top: 126px; }
  .card--back { top: 671px; }

  /* front */
  .brand {
    position: absolute; color: var(--mint);
    font-weight: 700; text-transform: uppercase; line-height: 1;
  }
  .brand--small { left: 22px; top: 18px; font-size: 80px; letter-spacing: 4px; }
  .brand-line {
    position: absolute; font-weight: 400;
    text-transform: uppercase; line-height: 1;
  }
  .brand-line--small { left: 193px; top: 98px; font-size: 18px; letter-spacing: 1px; color: var(--light-grey); }
  .contact-name {
    position: absolute; left: 24px; top: 220px;
    font-size: 43px; font-weight: 700; color: var(--white); line-height: 1;
  }
  .contact-line {
    position: absolute; left: 24px; font-size: 19px; color: var(--white); line-height: 1;
  }
  .contact-line--direct { top: 266px; }
  .contact-line--email { top: 293px; }
  .company-address {
    position: absolute; left: 0; width: 100%; text-align: center;
    color: var(--white); font-size: 19px; line-height: 1;
  }
  .company-address--street { top: 356px; }
  .company-address--town { top: 384px; }
  .company-address--phones { top: 417px; }

  /* back */
  .texture {
    position: absolute; right: 0; top: 0; width: 420px; height: 300px;
    background: radial-gradient(ellipse at 80% 20%, rgba(255,255,255,0.07), rgba(255,255,255,0) 70%);
  }
  .brand--large {
    left: 50%; transform: translateX(-50%); top: 128px;
    font-size: 160px; letter-spacing: 14px; white-space: nowrap;
  }
  .brand-line--large { right: 66px; top: 290px; font-size: 44px; letter-spacing: 2px; color: var(--grey); }
  .web-address {
    position: absolute; left: 0; width: 100%; top: 382px; text-align: center;
    font-family: "Didact Gothic", "Century Gothic", sans-serif;
    font-size: 38px; font-weight: 400; color: var(--white); line-height: 1;
    letter-spacing: 1.5px; -webkit-text-stroke: 1px var(--white);
  }
</style>
</head>
<body>
<main class="sheet">
  <h2 class="side-label side-label--front">Front</h2>
  <section class="card card--front">
    <div class="brand brand--small">Plume</div>
    <div class="brand-line brand-line--small">Sourcing</div>
    <p class="contact-name">Dorian Hartley</p>
    <p class="contact-line contact-line--direct">Direct Line: 020 7946 0518</p>
    <p class="contact-line contact-line--email">dorian@plumesourcing-mail.test</p>
    <p class="company-address company-address--street">Plume Sourching Ltd. • 58 - 60 Fenwick Row</p>
    <p class="company-address company-address--town">Hollin . Marbury • NW3 5QJ</p>
    <p class="company-address company-address--phones">Switchboard: 020 7946 0733 &nbsp;• &nbsp;Fax: 020 7946 0733</p>
  </section>

  <h2 class="side-label side-label--back">Back</h2>
  <section class="card card--back">
    <div class="texture" role="img" aria-label="Faint scattered square texture"></div>
    <div class="brand brand--large">Plume</div>
    <div class="brand-line brand-line--large">Sourcing</div>
    <p class="web-address">www.plumesourcing-mail.test</p>
  </section>
</main>
</body>
</html>
```